We do the same thing as http://quarrytrades.com. We are called harborbets.com. Need a fast loading website which targets the same demographics as quarrytrades.com. That means a website that is full of energy and excitement, capture concepts of volcano, explosiveness and profit.

Use all content from their site as placeholder.

```html
<!DOCTYPE html>
<html lang="en">
<head>
<meta charset="utf-8">
<title>Harbor Bets – Free Daily Penny Stock Picks</title>
<link rel="stylesheet" href="https://fonts.googleapis.com/css2?family=Anton&family=Oswald:wght@400;500;700&family=Roboto+Condensed:wght@400;700&family=Open+Sans:wght@400;600&display=swap">
<style>
:root{
  --bg:#0b0b0b;
  --band:#1b1b1b;
  --card:#212121;
  --white:#ffffff;
  --muted:#dcdcdc;
  --red:#e40a0a;
  --red-dark:#a30000;
  --orange:#f28a1c;
  --orange-dark:#c95a00;
  --orange-light:#ffb35a;
}
*{margin:0;padding:0;box-sizing:border-box}
html,body{width:918px;height:1200px;overflow:hidden}
body{background:var(--bg);color:var(--white);position:relative;font-family:"Roboto Condensed",Arial,sans-serif}
.abs{position:absolute}

.brand{left:74px;top:34px;font-family:"Anton",sans-serif;font-size:54px;line-height:60px;color:var(--red);letter-spacing:.5px}
.tollfree{left:505px;top:66px;font-family:"Oswald",sans-serif;font-size:18px;color:var(--white);letter-spacing:.3px}
.email-btn{left:675px;top:64px;width:166px;height:29px;border-radius:4px;background:linear-gradient(#e42020,var(--red-dark));border:1px solid #ff5a5a;display:flex;align-items:center;justify-content:center;gap:8px;font-family:"Open Sans",sans-serif;font-weight:600;font-size:10.5px;color:var(--white)}

.orange-bar{background:linear-gradient(var(--orange-light) 0%,var(--orange) 45%,var(--orange-dark) 100%);border-radius:6px;display:flex;align-items:center;justify-content:center;font-family:"Anton",sans-serif;color:var(--white);text-shadow:0 2px 4px rgba(0,0,0,.55);box-shadow:0 3px 8px rgba(0,0,0,.6)}
.top-banner{left:69px;top:105px;width:774px;height:60px;font-size:40px;z-index:2}

.slider{left:72px;top:160px;width:771px;height:376px;background:#151515;border-radius:0 0 4px 4px}
.slide-art{left:79px;top:165px;width:757px;height:365px;background:radial-gradient(ellipse at 55% 55%,#ff9a2a 0%,#c43d00 22%,#4a0d00 45%,#080303 70%)}
.slide-panel{left:230px;top:222px;width:240px;height:233px;background:rgba(60,60,60,.35)}
.slide-title{left:153px;top:283px;font-weight:700;font-size:41px;line-height:44px;text-shadow:0 2px 4px rgba(0,0,0,.7)}
.red-btn{background:linear-gradient(#e93030,var(--red-dark));border:1px solid #ff6b6b;border-radius:6px;font-family:"Anton",sans-serif;color:var(--white);display:flex;align-items:center;justify-content:center;text-shadow:0 1px 2px rgba(0,0,0,.6)}
.slide-btn{left:158px;top:395px;width:205px;height:37px;font-size:26px}
.arrow{top:298px;width:34px;height:68px;background:#1e1e1e;display:flex;align-items:center;justify-content:center}
.arrow.prev{left:72px;border-radius:0 34px 34px 0}
.arrow.next{left:809px;border-radius:34px 0 0 34px}

.signup-band{left:0;top:561px;width:918px;height:96px;background:var(--band)}
.signup-input{left:132px;top:582px;width:480px;height:52px;background:var(--white);border-radius:3px;font-family:"Oswald",sans-serif;font-size:24px;color:#8a8a8a;padding-left:22px;display:flex;align-items:center}
.signup-btn{left:601px;top:578px;width:197px;height:60px;font-family:"Oswald",sans-serif;font-size:29px}

.card{top:699px;width:243px;height:321px;background:var(--card);border-radius:4px}
.card-title{position:absolute;right:18px;top:13px;width:165px;text-align:right;font-weight:700;font-size:19px;line-height:23px}
.ribbon{position:absolute;left:-8px;top:-8px}
.card-art{position:absolute;left:8px;top:67px;width:227px;height:110px;border-radius:8px}
.card-text{position:absolute;left:10px;top:187px;width:223px;text-align:center;font-family:"Open Sans",sans-serif;font-size:10.5px;line-height:19.5px;color:var(--muted)}
.card-btn{position:absolute;left:40px;top:270px;width:166px;height:30px;font-size:18px}

.bottom-banner{left:114px;top:1053px;width:684px;height:60px;font-size:42px}
.bottom-banner .hot{color:var(--red);margin-left:12px}

.footer-rule{left:74px;top:1155px;width:770px;height:1px;background:#222}
.footer-text{left:0;top:1168px;width:918px;text-align:center;font-family:"Open Sans",sans-serif;font-size:10px;color:var(--white)}
</style>
</head>
<body>

<header>
  <div class="abs brand">HARBORBETS</div>
  <div class="abs tollfree">TOLL FEE (555) 240-3187</div>
  <div class="abs email-btn">
    <svg width="15" height="11" viewBox="0 0 15 11"><rect x=".5" y=".5" width="14" height="10" fill="none" stroke="#fff"/><path d="M.5 .5 7.5 6 14.5 .5" fill="none" stroke="#fff"/></svg>
    info@harborbets.com
  </div>
</header>

<div class="abs orange-bar top-banner">SIGN UP FREE FOR HARBOR BETS</div>

<section>
  <div class="abs slider"></div>
  <div class="abs slide-art" role="img" aria-label="Flaming percent sign on a black background"></div>
  <div class="abs slide-panel"></div>
  <h1 class="abs slide-title">FREE Daily Penny<br>Stocks Picks</h1>
  <div class="abs red-btn slide-btn">READ MORE</div>
  <div class="abs arrow prev"><svg width="14" height="18" viewBox="0 0 14 18"><path d="M11 2 4 9l7 7" fill="none" stroke="#fff" stroke-width="3.5"/></svg></div>
  <div class="abs arrow next"><svg width="14" height="18" viewBox="0 0 14 18"><path d="M3 2l7 7-7 7" fill="none" stroke="#fff" stroke-width="3.5"/></svg></div>
</section>

<section>
  <div class="abs signup-band"></div>
  <div class="abs signup-input">Sign in here</div>
  <div class="abs orange-bar signup-btn">SIGN UP NOW</div>
</section>

<section>
  <article class="abs card" style="left:79px">
    <svg class="ribbon" width="112" height="92" viewBox="0 0 112 92"><path d="M0 70 70 0h38L0 92z" fill="#e98320"/><circle cx="40" cy="40" r="27" fill="#f08a22"/><text x="40" y="32" text-anchor="middle" font-family="Anton,sans-serif" font-size="9" fill="#fff">GREAT</text><text x="40" y="50" text-anchor="middle" font-family="Anton,sans-serif" font-size="17" fill="#fff">SALE</text></svg>
    <h2 class="card-title">FREE Daily Penny Stocks Picks</h2>
    <div class="card-art" role="img" aria-label="Flaming flower on black" style="background:radial-gradient(ellipse at 50% 55%,#ff8a1e 0%,#a82400 35%,#120404 70%)"></div>
    <p class="card-text">Our newsletters are completely FREE. We do not charge anything to our subscribers. Feel free to share our website with your family &amp; friends.</p>
    <div class="red-btn card-btn">READ MORE</div>
  </article>

  <article class="abs card" style="left:336px">
    <svg class="ribbon" width="112" height="92" viewBox="0 0 112 92"><path d="M0 70 70 0h38L0 92z" fill="#e98320"/><circle cx="40" cy="40" r="27" fill="#f08a22"/><text x="40" y="32" text-anchor="middle" font-family="Anton,sans-serif" font-size="9" fill="#fff">GREAT</text><text x="40" y="50" text-anchor="middle" font-family="Anton,sans-serif" font-size="17" fill="#fff">SALE</text></svg>
    <h2 class="card-title">Harbor Stock Picks!!!</h2>
    <div class="card-art" role="img" aria-label="Burning playing cards and poker chip" style="background:radial-gradient(ellipse at 50% 50%,#f6b54a 0%,#b44a08 30%,#0c0505 62%)"></div>
    <p class="card-text">Our newsletters are completely FREE. We do not charge anything to our subscribers. Feel free to share our website with your family &amp; friends.</p>
    <div class="red-btn card-btn">READ MORE</div>
  </article>

  <article class="abs card" style="left:593px">
    <svg class="ribbon" width="112" height="92" viewBox="0 0 112 92"><path d="M0 70 70 0h38L0 92z" fill="#e98320"/><circle cx="40" cy="40" r="27" fill="#f08a22"/><text x="40" y="32" text-anchor="middle" font-family="Anton,sans-serif" font-size="9" fill="#fff">GREAT</text><text x="40" y="50" text-anchor="middle" font-family="Anton,sans-serif" font-size="17" fill="#fff">SALE</text></svg>
    <h2 class="card-title">FREE Stock Alerts</h2>
    <div class="card-art" role="img" aria-label="Flaming at sign in smoke" style="background:radial-gradient(ellipse at 50% 50%,#ff7a1e 0%,#8e1c04 32%,#161313 68%)"></div>
    <p class="card-text">Our newsletters are completely FREE. We do not charge anything to our subscribers. Feel free to share our website with your family &amp; friends.</p>
    <div class="red-btn card-btn">READ MORE</div>
  </article>
</section>

<div class="abs orange-bar bottom-banner">SIGN UP FREE FOR<span class="hot">NEWSLETTER</span></div>

<footer>
  <div class="abs footer-rule"></div>
  <p class="abs footer-text">Serving Coastline, &nbsp;LLC 48 Ember Quay Suite 210, Portside, OH 40012 (P) 555-240-3187</p>
</footer>

</body>
</html>
```